Proverbs Sermon Series Artwork

We are in need of new artwork for an upcoming sermon series that our Senior Pastor will be preaching for at least the next 6 months. This graphic will be used extensively on our app, website, and in worship services and needs to be of excellent quality and also provide meaning behind the entirety of the series. Proverbs is a very rich book of the Bible that deals with wisdom and how to live according to God's principles. The graphic needs to reflect this truth and communicate to those who see it that there are different ways that each of us can choose to live.
We are very flexible on the goal of this piece and don't really have anything in mind. The graphic that is the most professional but also communicated the goal of the sermon series will be the one selected. Please see the must haves to get an idea of different formats we would like to use this graphic in. It will be a key image in the life of our church over the next 6-12 months.
Thanks for looking into this project. I hope you will submit a graphic design and use your God given talents to help us (and make a little money on the side). ArtFolio has served us well in the past and we are excited to use it again.
Updates
As of right now, I have 3 good designs from 2 designers. I would love to see the edits made based on feedback provided. I think there is a lot of potential in all 3 designs. If you have questions please let me know. After all artwork is submitted I will be presenting it to the senior pastor and he will select the one he likes the best. I would like to bring him 5 designs so there is still room for some other good submissions from new designers! Also, I uploaded a road sign image. I would like to see something with an image like that from someone.
Target Market(s)
Church members, app users, website visitors
Industry/Entity Type
Religious
Requirements
Must have
- Artwork must include Proverbs in a bold easy to read font. The graphic must also lend itself to different formats. 1920x1080 wide format graphic, 1024x1024 square icon, 1920x692 banner.
Nice to have
- The sermon series is about us having choices on how to live our lives and the goal that we should take God's way instead of ours. This would lend itself well to road signs or maybe something cool with nature. Maybe even a word art as proverbs is a lot of sayings that speak to wisdom of the Christian walk. I'm pretty flexible.
Should not have
- Not overly feminine like most church artwork. This is geared to the whole body, not women.

```html
<!DOCTYPE html>
<html lang="en">
<head>
<meta charset="UTF-8">
<title>Proverbs Sermon Series Banner</title>
<link rel="stylesheet" href="https://fonts.googleapis.com/css2?family=Caveat+Brush&display=swap">
<style>
  :root {
    --frame: #ffffff;
    --sky-glow: #fde9b0;
    --sky-gold: #e9a53a;
    --sky-amber: #b8701f;
    --sky-dusk: #5a3c24;
    --sky-cool: #9aa6ad;
    --lettering: #ecebe8;
    --lettering-shadow: rgba(30, 18, 8, 0.75);
  }
  html, body {
    margin: 0;
    padding: 0;
    width: 1200px;
    height: 432px;
    overflow: hidden;
    background: var(--frame);
  }
  .banner {
    position: relative;
    width: 1200px;
    height: 432px;
    background: var(--frame);
    overflow: hidden;
  }
  .sunset-photo {
    position: absolute;
    left: 10px;
    top: 6px;
    width: 1180px;
    height: 420px;
    background:
      radial-gradient(ellipse 30% 45% at 40% 62%, var(--sky-glow) 0%, rgba(233, 165, 58, 0) 100%),
      radial-gradient(ellipse 25% 35% at 74% 18%, rgba(154, 166, 173, 0.55) 0%, rgba(154, 166, 173, 0) 100%),
      linear-gradient(180deg, var(--sky-dusk) 0%, var(--sky-amber) 30%, var(--sky-gold) 60%, var(--sky-amber) 85%, var(--sky-dusk) 100%);
  }
  .series-title {
    position: absolute;
    left: 0;
    width: 1200px;
    margin: 0;
    text-align: center;
    font-family: "Caveat Brush", cursive;
    font-weight: 400;
    color: var(--lettering);
    text-shadow: 3px 4px 6px var(--lettering-shadow);
  }
  .series-name {
    top: 88px;
    font-size: 54px;
    line-height: 60px;
    letter-spacing: 3px;
  }
  .series-quote {
    top: 168px;
    font-size: 84px;
    line-height: 98px;
    letter-spacing: 3px;
  }
</style>
</head>
<body>
  <main class="banner">
    <div class="sunset-photo" role="img" aria-label="Photograph of a golden sunset over calm water with dark hills and clouds"></div>
    <h1 class="series-title series-name">PROVERBS</h1>
    <p class="series-title series-quote">"TRUST IN THE LORD WITH ALL<br>YOUR HEART."</p>
  </main>
</body>
</html>
```